International Marketing Company - Web Design Project

kVesta is a well-funded start up in London developing an Online Marketing Platform for small businesses in Europe.

We require a large number of high quality business web designs for our business website builder. Our business websites are completely integrated into our Online Marketing systems and therefore it is important for designers to comply with our Design Guidelines.

This initial contest is a trial for us to open up the design process to top designers for the Builders vertical (e.g. Builders, Electricians, Plumbers, Flooring, etc.). We have implemented a base html structure and design and included them in the files.

Use your creativity to design new and fresh designs based on the included elements (e.g. testimonials, business description, etc).

We will award the stated prize money for the top three designs.

Any designers that submit designs we feel are of a high enough quality but do not make the top 3 could still be compensated and WILL be invited to participate in our next vertical competition.

Therefore, we encourage designers to submit as many designs as possible as we may award up to 25 designs.

Submissions will be reviewed daily and feedback provided where possible.

Designers who can also code will have the options to implement their designs for an additional fee.

Good luck!
Updates

There has been a mistake made in regard to the prize. Pixel Harbor should have it fixed soon.

1st place = £350
2nd place = £250
3rd Place = £150

Thanks,
Dorian
25/11/2011

UPDATE:

1st place will win £350
2nd place will win £250
3rd place will win £150

Everything else is as to the specification.

Thanks
Dorian

Target Market(s)

Builders, Electricians, Plumbers, Tradesman, Small construction companies

Industry/Entity Type

Business

Requirements
Must have
• Totally new designs based around the elements we want to show on each page.

We are looking for something different to the design we already have. But you can use that as a starting point.

Use the included files to see what is required for each page. Here is a brief outline:

Homepage - Testimonials, News, Business Description, Latest Projects and Call to action

About-Us - Team Summary, About the Business and a call to action

Projects Page - Project Details (Oage Title and description), Each project needs a title, content and 2 images.

Testimonials Page - The testifiers name and their comment

Contacts Page - Trovix Map, Company address, business hours, contact form and a call to action.

Please submit final designs in Photoshop or Fireworks format.

Each page has a set of elements. These element must feature in the design of that page. See supporting documents for page details.

All elements must be included in your design. Please do not add any extra element.

Professional look and feel
Nice to have
• Design variations:
Full width designs
Boxed Designs
With AND without carousels
OR static images
Good use of stock images.

Creative use of the elements, dont be restricted/influenced by the default design we have already

Designs based on the 960 grid

```html
<!DOCTYPE html>
<html lang="en">
<head>
<meta charset="utf-8">
<title>kVesta — Quick, Solid, Quality</title>
<link href="https://fonts.googleapis.com/css2?family=Arimo:wght@400;700&family=PT+Sans:wght@400;700&display=swap" rel="stylesheet">
<style>
:root{
  --ink:#111;
  --text:#222;
  --muted:#666;
  --orange:#f7941d;
  --orange-soft:#f9963a;
  --yellow:#fec20f;
  --dark-btn:#1e1e1e;
  --nav-bg:#e4e4e4;
  --nav-line:#b9b9b9;
  --rule:#b5b5b5;
  --field:#cfcfcf;
  --white:#fff;
}
*{box-sizing:border-box;margin:0;padding:0}
html,body{width:969px;height:1200px;overflow:hidden;background:var(--white)}
body{position:relative;font-family:Arimo,Arial,sans-serif;color:var(--text)}
.abs{position:absolute}
.top-bar{left:0;top:0;width:969px;height:4px;background:#333}
.brand{left:37px;top:18px;font-family:"PT Sans",sans-serif;font-size:42px;font-weight:400;color:var(--ink);line-height:1}
.tagline{left:39px;top:71px;font-size:14.5px;color:var(--ink)}
.tagline .dot{display:inline-block;width:7px;height:7px;border-radius:50%;background:var(--orange);margin:0 6px;vertical-align:2px}
.call{left:328px;top:9px;font-size:14px;font-weight:700;color:var(--ink)}
.call span{color:var(--orange)}
.quote-link{left:758px;top:7px;font-size:12px;color:var(--muted)}
.quote-badge{left:898px;top:-22px;width:50px;height:50px;border-radius:50%;background:var(--orange)}
.nav{left:325px;top:38px;width:612px;height:41px;background:linear-gradient(#efefef,#dcdcdc);border:1px solid #cfcfcf;border-radius:4px;display:flex;align-items:center;font-size:15px;color:#444}
.nav a{color:inherit;text-decoration:none;height:100%;display:flex;align-items:center;justify-content:center;border-right:1px solid var(--nav-line)}
.nav a:last-child{border-right:0}
.nav .is-active{background:var(--orange);color:var(--white);border-radius:3px 0 0 3px;border-right:0}
.hero-image{left:15px;top:135px;width:320px;height:335px;background:linear-gradient(180deg,#fff 0%,#e6eaee 45%,#b9c2cc 100%)}
.slide-dots{left:25px;top:472px;display:flex;gap:4px}
.slide-dots i{width:9px;height:9px;background:#ccc;display:block}
.slide-dots i.on{background:var(--orange)}
.slogan{left:517px;top:163px;font-family:"PT Sans",sans-serif;color:#666}
.slogan .improving{font-size:29px;letter-spacing:8px;line-height:1}
.slogan .peoples{font-size:30px;margin-top:4px;line-height:1;color:#6a6a6a}
.slogan .life{position:absolute;left:132px;top:30px;font-size:76px;font-weight:700;color:#000;line-height:1;letter-spacing:-1px}
.service{top:269px;height:201px;border-radius:3px;color:var(--white);padding:12px 0 0 21px;font-family:"PT Sans",sans-serif}
.service h2{font-size:26px;font-weight:400;margin-bottom:6px}
.service ul{list-style:none;font-family:Arimo,Arial,sans-serif;font-size:14.5px}
.service li{height:34px;padding-left:16px;position:relative}
.service li::before{content:"";position:absolute;left:0;top:6px;width:6px;height:6px;border-radius:50%;background:var(--bullet)}
.svc-building{left:333px;width:204px;background:var(--orange);--bullet:#ffd23a}
.svc-infra{left:539px;width:203px;background:var(--orange-soft);--bullet:#fff}
.svc-env{left:745px;width:203px;background:var(--yellow);--bullet:#f7941d}
.btn{display:flex;align-items:center;justify-content:center;background:linear-gradient(#3a3a3a,#111);color:var(--white);font-size:12.5px;border-radius:4px;width:106px;height:32px}
.heading{font-family:"PT Sans",sans-serif;font-size:29px;color:var(--ink);font-weight:400;line-height:1}
.welcome-lead{left:22px;top:575px;width:632px;font-size:11.5px;font-weight:700;color:#000;line-height:18px}
.welcome-body{left:22px;top:621px;width:635px;font-size:11.6px;line-height:17.6px;color:#222}
.proj-img{background:linear-gradient(160deg,#c7d6e8,#8fa3b8)}
.proj-steel{left:37px;top:850px;width:183px;height:221px;background:linear-gradient(170deg,#6d95c7,#cfd9e4 60%,#9aa6b2)}
.proj-worker{left:220px;top:831px;width:225px;height:240px;background:linear-gradient(160deg,#8f8a82,#5a5147 55%,#3b342d)}
.proj-interior{left:445px;top:855px;width:177px;height:212px;background:linear-gradient(180deg,#eee9e2,#c9a57a 70%,#a8743f)}
.proj-caption{left:220px;top:1014px;width:225px;height:57px;background:rgba(20,20,20,.78);color:var(--white);font-size:11.5px;line-height:18px;padding:10px 14px}
.arrow{width:20px;height:40px;background:#222;border-radius:3px;display:flex;align-items:center;justify-content:center}
.news{left:682px;width:270px;display:flex;gap:9px}
.news p{font-size:11.5px;line-height:17.5px;color:#111}
.date{color:var(--orange);font-size:11.5px}
.testi-photo{left:690px;top:884px;width:84px;height:75px;border:1px solid #ccc;padding:3px;background:#fff}
.testi-photo div{width:100%;height:100%;background:linear-gradient(160deg,#9cc3e6,#dfe9f2 60%,#e07a3a)}
.testi-name{left:787px;top:917px;font-size:11.5px;font-weight:700;color:#000}
.testi-date{left:787px;top:935px}
.testi-text{left:687px;top:968px;width:270px;font-size:11.5px;line-height:18px;color:#111}
.footer-rule{left:17px;top:1111px;width:931px;height:2px;background:var(--rule)}
.newsletter{left:28px;top:1130px;font-size:11.5px;color:#333}
.news-field{left:89px;top:1127px;width:143px;height:21px;background:var(--field)}
.news-go{left:232px;top:1127px;width:25px;height:21px;background:var(--orange);color:#fff;font-size:13px;display:flex;align-items:center;justify-content:center;font-weight:700}
.connect{left:742px;top:1128px;font-size:11.5px;color:#333}
.social{top:1122px;width:28px;height:28px;border-radius:4px}
.copyright{left:27px;top:1164px;font-size:11.5px;color:#333}
.copyright b{color:var(--orange)}
.footer-links{right:28px;top:1165px;font-size:11.5px;color:#333}
</style>
</head>
<body>
<div class="abs top-bar"></div>

<header>
  <div class="abs brand">kVesta</div>
  <div class="abs tagline">Quick<span class="dot"></span>Solid<span class="dot"></span>Quality</div>
  <div class="abs call">Call <span>020 7946 0321</span></div>
  <div class="abs quote-link">Click here to Get a Qute →</div>
  <div class="abs quote-badge">
    <svg width="50" height="50" viewBox="0 0 50 50"><path d="M18 30l7 5 7-5M18 36l7 5 7-5" fill="none" stroke="#fff3c0" stroke-width="2"/></svg>
  </div>
  <nav class="abs nav">
    <a class="is-active" style="width:89px">HOME</a>
    <a style="width:118px">ABOUT US</a>
    <a style="width:155px">TESTIMONIALS</a>
    <a style="width:119px">PORTFOLIO</a>
    <a style="width:130px">CONTACTS</a>
  </nav>
</header>

<section class="hero">
  <div class="abs hero-image" role="img" aria-label="Tower block under construction with cranes"></div>
  <div class="abs slide-dots"><i></i><i class="on"></i><i></i><i></i></div>
  <div class="abs slogan">
    <div class="improving">IMPROVING</div>
    <div class="peoples">peoples's</div>
    <div class="life">life</div>
  </div>

  <div class="abs service svc-building">
    <h2>Building</h2>
    <ul><li>Structural Engneering</li><li>Building Services</li><li>Site Infrastructure</li><li>Speculist Consulting</li></ul>
  </div>
  <div class="abs service svc-infra">
    <h2>Infrastructure</h2>
    <ul><li>Structural Engneering</li><li>Building Services</li><li>Site Infrastructure</li><li>Speculist Consulting</li></ul>
  </div>
  <div class="abs service svc-env">
    <h2>Environment</h2>
    <ul><li>Structural Engneering</li><li>Building Services</li><li>Site Infrastructure</li><li>Speculist Consulting</li></ul>
  </div>
  <div class="abs btn" style="left:383px;top:453px">Read more</div>
  <div class="abs btn" style="left:588px;top:453px">Read more</div>
  <div class="abs btn" style="left:794px;top:453px">Read more</div>
</section>

<main>
  <h1 class="abs heading" style="left:22px;top:521px">Welcome !</h1>
  <p class="abs welcome-lead">At vero eos et accusamus et iusto odio dignissimos ducimus qui blanditiis praesentium voluptatum deleniti atque corrupti quos dolores</p>
  <p class="abs welcome-body">At vero eos et accusamus et iusto odio dignissimos ducimus qui blanditiis praesentium voluptatum deleniti atque corrupti quos dolores et quas molestias excepturi sint occaecati cupiditate non provident, similique sunt in culpa qui officia deserunt mollitia animi, id est laborum et dolorum fuga. Et harum quidem rerum facilis est et expedita distinctio. Nam libero tempore, cum soluta nobis est eligendi optio cumque nihil impedit quo minus id quod maxime placeat facere possimus, omnis voluptas assumenda est, omnis dolor repellendus. Temporibus autem quibusdam et aut officiis debitis aut rerum necessitatibus saepe eveniet ut et voluptates repudiandae sint et molestiae non recusandae. Itaque earum rerum hic tenetur a sapiente delectus, ut aut reiciendis voluptatibus maiores alias consequatur aut perferendis doloribus asperiores repellat.</p>

  <h2 class="abs heading" style="left:22px;top:788px">Projects</h2>
  <div class="abs proj-steel" role="img" aria-label="Steel frame of a building against blue sky"></div>
  <div class="abs proj-interior" role="img" aria-label="Finished open-plan interior with wooden floor"></div>
  <div class="abs proj-worker" role="img" aria-label="Builder in hard hat guiding a concrete panel"></div>
  <div class="abs proj-caption">Lorem Ipsum is simply dummy text of the printing and typesetting industry.</div>
  <div class="abs arrow" style="left:19px;top:1013px"><svg width="8" height="14"><path d="M7 1L2 7l5 6" fill="none" stroke="#fff" stroke-width="2"/></svg></div>
  <div class="abs arrow" style="left:627px;top:1013px"><svg width="8" height="14"><path d="M1 1l5 6-5 6" fill="none" stroke="#fff" stroke-width="2"/></svg></div>
</main>

<aside>
  <h2 class="abs heading" style="left:685px;top:521px">Laest News</h2>
  <div class="abs news" style="top:571px">
    <svg width="42" height="50" viewBox="0 0 42 50"><rect x="1" y="5" width="40" height="44" rx="3" fill="#fff" stroke="#8a9aa8"/><rect x="1" y="5" width="40" height="12" rx="3" fill="#4a86c0"/><rect x="8" y="1" width="4" height="9" rx="2" fill="#999"/><rect x="30" y="1" width="4" height="9" rx="2" fill="#999"/><text x="21" y="39" font-family="Arial" font-size="15" font-weight="700" text-anchor="middle" fill="#111">24</text></svg>
    <div><p>Lorem Ipsum is simply dummy text of the printing and typesetting industry.</p><div class="date">Dec 04,2011</div></div>
  </div>
  <div class="abs news" style="top:647px">
    <svg width="42" height="50" viewBox="0 0 42 50"><rect x="1" y="5" width="40" height="44" rx="3" fill="#fff" stroke="#8a9aa8"/><rect x="1" y="5" width="40" height="12" rx="3" fill="#4a86c0"/><rect x="8" y="1" width="4" height="9" rx="2" fill="#999"/><rect x="30" y="1" width="4" height="9" rx="2" fill="#999"/><text x="21" y="39" font-family="Arial" font-size="15" font-weight="700" text-anchor="middle" fill="#111">24</text></svg>
    <div><p>Lorem Ipsum is simply dummy text of the printing and typesetting industry.</p><div class="date">Dec 04,2011</div></div>
  </div>
  <div class="abs news" style="top:723px">
    <svg width="42" height="50" viewBox="0 0 42 50"><rect x="1" y="5" width="40" height="44" rx="3" fill="#fff" stroke="#8a9aa8"/><rect x="1" y="5" width="40" height="12" rx="3" fill="#4a86c0"/><rect x="8" y="1" width="4" height="9" rx="2" fill="#999"/><rect x="30" y="1" width="4" height="9" rx="2" fill="#999"/><text x="21" y="39" font-family="Arial" font-size="15" font-weight="700" text-anchor="middle" fill="#111">24</text></svg>
    <div><p>Lorem Ipsum is simply dummy text of the printing and typesetting industry.</p><div class="date">Dec 04,2011</div></div>
  </div>
  <div class="abs btn" style="left:837px;top:783px">More News</div>

  <h2 class="abs heading" style="left:685px;top:841px">Testimonials</h2>
  <div class="abs testi-photo"><div role="img" aria-label="Portrait of a builder in a hard hat"></div></div>
  <div class="abs testi-name">Quos dolores</div>
  <div class="abs date testi-date">Dec 04,2011</div>
  <p class="abs testi-text">Typeline sheets containing Lorem Ipsum passages, and more recently with desktop publishing software like Folio Setter</p>
  <div class="abs btn" style="left:837px;top:1031px">Read more</div>
</aside>

<footer>
  <div class="abs footer-rule"></div>
  <div class="abs newsletter">Newsletter</div>
  <div class="abs news-field"></div>
  <div class="abs news-go">›</div>
  <div class="abs connect">Connect with us on</div>
  <div class="abs social" style="left:846px;background:#2f6db5"></div>
  <div class="abs social" style="left:879px;background:#5aaee0"></div>
  <div class="abs social" style="left:912px;background:#f08a1c"></div>
  <div class="abs copyright">2011 © Copyrights.<b>www.kvesta.com</b>.received</div>
  <div class="abs footer-links">Home | About us | Testimonials | Portfolio | Contacts</div>
</footer>
</body>
</html>
```